Poloshirt Packaging

We need a very attractive packaging design for our poloshirts. We are wholesaler of the schoolwear market. See what we currently have. I dont want any specific sizing put on the packaging. One design for all poloshirts (2 sides).
our logo is attached aswell

Target Market(s)

Parents

Requirements
Must have
• Our logo
Should not have
• size or age

```html
<!DOCTYPE html>
<html lang="en">
<head>
<meta charset="utf-8">
<title>Stridewell Poloshirt Packaging</title>
<link rel="stylesheet" href="https://fonts.googleapis.com/css2?family=Mulish:wght@700;800&display=swap">
<style>
  :root {
    --navy: #0b3160;
    --red: #e2312b;
    --deep-red: #de2c25;
    --orange-red: #e24a24;
    --amber: #f2aa1c;
    --yellow: #f7d41a;
    --sheet: #ffffff;
    --outline: #222222;
    --shadow: #b9b9b9;
    --page: #ffffff;
  }
  html, body {
    margin: 0;
    padding: 0;
    width: 1200px;
    height: 873px;
    overflow: hidden;
    background: var(--page);
  }
  .packaging {
    display: block;
    width: 1200px;
    height: 873px;
  }
  .panel-shadow { fill: var(--shadow); }
  .panel { fill: var(--sheet); stroke: var(--outline); stroke-width: 0.8; }
  .brand-name {
    font-family: "Mulish", "Century Gothic", sans-serif;
    font-weight: 800;
    fill: var(--navy);
  }
  .product-name {
    font-family: "Mulish", "Century Gothic", sans-serif;
    font-weight: 800;
    fill: var(--red);
  }
  .feature-bar { fill: var(--navy); }
  .feature-text {
    font-family: "Mulish", "Century Gothic", sans-serif;
    font-weight: 700;
    font-size: 7.6px;
    fill: #ffffff;
  }
  .decor-area { opacity: 0.55; }
</style>
</head>
<body>
<svg class="packaging" viewBox="0 0 977 711" xmlns="http://www.w3.org/2000/svg" aria-label="Two sides of the Stridewell poloshirt package">
  <defs>
    <linearGradient id="warm-front" x1="0" y1="0" x2="1" y2="0">
      <stop offset="0" stop-color="var(--orange-red)"/>
      <stop offset="1" stop-color="var(--amber)"/>
    </linearGradient>
    <linearGradient id="warm-back" x1="0" y1="0" x2="1" y2="0">
      <stop offset="0" stop-color="var(--yellow)"/>
      <stop offset="0.5" stop-color="var(--amber)"/>
      <stop offset="1" stop-color="var(--orange-red)"/>
    </linearGradient>
    <linearGradient id="red-soft" x1="0" y1="0" x2="1" y2="0">
      <stop offset="0" stop-color="var(--deep-red)" stop-opacity="0.6"/>
      <stop offset="1" stop-color="var(--deep-red)"/>
    </linearGradient>
  </defs>

  <rect class="panel-shadow" x="22" y="24" width="939" height="665"/>

  <g class="side side-front">
    <rect class="panel" x="18" y="20" width="469" height="665"/>
    <rect class="decor-area" x="18.4" y="150" width="468.2" height="270" fill="url(#warm-front)"
      role="img" aria-label="Flowing ribbon decoration in red to amber"/>
    <rect class="decor-area" x="295" y="578" width="191.6" height="106.6" fill="url(#red-soft)"
      role="img" aria-label="Red corner swoosh decoration"/>
    <text class="brand-name" x="60" y="497" font-size="62" textLength="355" lengthAdjust="spacingAndGlyphs">Stridewell</text>
    <text class="product-name" x="60" y="540" font-size="30" textLength="180" lengthAdjust="spacingAndGlyphs">POLOSHIRT</text>
    <rect class="feature-bar" x="60" y="561" width="295" height="15"/>
    <text class="feature-text" x="207.5" y="571.5" text-anchor="middle" textLength="280" lengthAdjust="spacingAndGlyphs">Superior weight fabric | Easy Care - Low iron | Reactive Dyes</text>
  </g>

  <g class="side side-back">
    <rect class="panel" x="487" y="20" width="470" height="665"/>
    <rect class="decor-area" x="487.4" y="355" width="469.2" height="135" fill="url(#warm-back)"
      role="img" aria-label="Flowing ribbon decoration in yellow to red"/>
    <rect class="decor-area" x="793" y="598" width="163.6" height="86.6" fill="url(#red-soft)"
      role="img" aria-label="Red corner swoosh decoration"/>
    <text class="brand-name" x="583" y="258" font-size="48" textLength="275" lengthAdjust="spacingAndGlyphs">Stridewell</text>
    <text class="product-name" x="719.5" y="345" font-size="30" text-anchor="middle" textLength="165" lengthAdjust="spacingAndGlyphs">POLOSHIRT</text>
  </g>
</svg>
</body>
</html>
```